Cosmetics Brand Logo and Bottle Label Design

We are creating a new cosmetics brand called "Nolan Whitby" and would like you to create an amazing logo and bottle label for this brand's new 100% pure argan oil product.
For the logo, we really like the logo's of Marin Calloway and Vessa. The text should be Sans Serif (without feet).
For the actual bottle label, please find attached labels of one of our competitors design which really like. We really like the simplicity and elegance of the design. The only difference is that our product will be using light turqoise as the brand color. Please feel free to add your own creativity into it as well.
Industry/Entity Type
Cosmetics
Logo Text
Nolan Whitby
Font styles to use

```html
<!DOCTYPE html>
<html lang="en">
<head>
<meta charset="utf-8">
<title>Nolan Whitby – Argan Oil Label</title>
<link rel="stylesheet" href="https://fonts.googleapis.com/css2?family=Lato:wght@300;400&display=swap">
<style>
  :root {
    --backdrop: #ebe1df;
    --label-turquoise: #a6dcd3;
    --label-glow: #f4fbfa;
    --brand-teal: #4fbfae;
    --soft-teal: #5ec6b6;
    --ink-white: #ffffff;
    --fine-print: #4a6460;
    --leaf-fill-a: #c9ece6;
    --leaf-fill-b: #a6dcd3;
  }
  html, body {
    margin: 0;
    padding: 0;
    width: 1200px;
    height: 1200px;
    overflow: hidden;
    background: var(--backdrop);
  }
  .canvas {
    position: relative;
    width: 1200px;
    height: 1200px;
  }
  .bottle-label {
    position: absolute;
    left: 40px;
    top: 256px;
    width: 1120px;
    height: 689px;
    box-shadow: 0 2px 6px rgba(0,0,0,0.12);
  }
  .brand-name {
    font-family: "Lato", sans-serif;
    font-weight: 300;
    font-size: 64px;
    fill: var(--brand-teal);
  }
  .product-line {
    font-family: "Lato", sans-serif;
    font-weight: 300;
    font-size: 40px;
    fill: var(--soft-teal);
  }
  .descriptor {
    font-family: "Lato", sans-serif;
    font-weight: 300;
    font-size: 38px;
    fill: var(--soft-teal);
  }
  .volume {
    font-family: "Lato", sans-serif;
    font-weight: 300;
    font-size: 32px;
    fill: var(--ink-white);
  }
  .fine-print {
    font-family: "Lato", sans-serif;
    font-weight: 400;
    font-size: 8.6px;
    fill: var(--fine-print);
  }
  .info-frame {
    fill: none;
    stroke: #c6ebe5;
    stroke-width: 1;
  }
</style>
</head>
<body>
<main class="canvas">
  <svg class="bottle-label" viewBox="0 0 972 598" xmlns="http://www.w3.org/2000/svg">
    <defs>
      <radialGradient id="label-glow" cx="0.3" cy="0.55" r="0.45">
        <stop offset="0" stop-color="var(--label-glow)" stop-opacity="0.95"/>
        <stop offset="0.6" stop-color="var(--label-glow)" stop-opacity="0.25"/>
        <stop offset="1" stop-color="var(--label-glow)" stop-opacity="0"/>
      </radialGradient>
      <linearGradient id="leaf-tone" x1="0" y1="0" x2="1" y2="1">
        <stop offset="0" stop-color="var(--leaf-fill-a)"/>
        <stop offset="1" stop-color="var(--leaf-fill-b)"/>
      </linearGradient>
    </defs>

    <rect class="label-base" width="972" height="598" fill="var(--label-turquoise)"/>
    <rect class="label-sheen" width="972" height="598" fill="url(#label-glow)"/>

    <text class="brand-name" transform="translate(202 547) rotate(-90)"
          textLength="500" lengthAdjust="spacing">NOLAN WHITBY</text>
    <text class="product-line" transform="translate(257 420) rotate(-90)"
          textLength="375" lengthAdjust="spacing">100% Pure Argan Oil</text>

    <rect class="leaf-illustration" x="312" y="215" width="160" height="185" rx="70"
          fill="url(#leaf-tone)" opacity="0.6" role="img"
          aria-label="Line illustration of argan leaves and berries"/>

    <text class="descriptor" x="292" y="458">organic</text>
    <text class="descriptor" x="292" y="502">moisturizing oil</text>
    <text class="volume" x="292" y="551">50ml 1.7 fl oz</text>

    <rect class="info-frame" x="715" y="65" width="230" height="475"/>
    <rect class="info-frame" x="875" y="85" width="60" height="95"/>

    <g class="info-panel" transform="translate(728 527) rotate(-90)">
      <text class="fine-print" x="0" y="10">We are creating a new cosmetics brand called "Nolan Whitby" and would like you to create an</text>
      <text class="fine-print" x="0" y="24">amazing logo and bottle label for this brand's new 100% pure argan oil product.</text>
      <text class="fine-print" x="0" y="56">For the logo, we really like the logo's of Marin Calloway and Vessa. The text should be Sans Serif</text>
      <text class="fine-print" x="0" y="70">(without feet).</text>
      <text class="fine-print" x="0" y="100">For the actual bottle label, please find attached labels of one of our competitors design which</text>
      <text class="fine-print" x="0" y="114">really like. We really like the simplicity and elegance of the design. The only difference is that our</text>
      <text class="fine-print" x="0" y="128">product will be using light turqoise as the brand color. Please feel free to add your own creativity</text>
      <text class="fine-print" x="0" y="142">into it as well.</text>
    </g>
  </svg>
</main>
</body>
</html>
```